Software engineering company needs business card

I need a cool business card. Company: Soft Belan Brindlewood Ave 41 58207 Harrowfield Name: Gerald Vanholt CEO / Managing Director & Owner

```html
<!DOCTYPE html>
<html lang="de">
<head>
<meta charset="utf-8">
<title>Belan Systems – Visitenkarte</title>
<link rel="stylesheet" href="https://fonts.googleapis.com/css2?family=Quicksand:wght@400;500;700&display=swap">
<style>
  :root {
    --backdrop: #e6e4e1;
    --card-white: #ffffff;
    --brand-green: #6cb72a;
    --ink-dark: #222222;
    --ink-light: #f2f7ec;
  }
  * { margin: 0; padding: 0; box-sizing: border-box; }
  html, body {
    width: 1200px; height: 788px; overflow: hidden;
    background: var(--backdrop);
    font-family: "Quicksand", sans-serif;
  }
  .card {
    position: absolute; top: 260px;
    width: 480px; height: 267px;
    overflow: hidden;
    box-shadow: 0 3px 10px rgba(0,0,0,0.18);
  }
  .card--front {
    left: 110px; background: var(--card-white);
    display: flex; align-items: center; justify-content: center;
  }
  .brand-name {
    font-weight: 700; color: var(--brand-green);
    letter-spacing: 3px; white-space: nowrap; text-transform: uppercase;
  }
  .card--front .brand-name { font-size: 34px; }
  .card--back { left: 635px; background: var(--brand-green); }
  .back-header {
    position: absolute; left: 0; top: 0; width: 100%; height: 74px;
    background: var(--ink-dark);
    display: flex; align-items: center; justify-content: center;
  }
  .back-header .brand-name { font-size: 20px; letter-spacing: 2px; }
  .name-band {
    position: absolute; left: 0; top: 92px; width: 100%; height: 61px;
    background: var(--card-white); text-align: center;
  }
  .name-band__notch {
    position: absolute; left: 50%; top: 0; transform: translateX(-50%);
  }
  .person-name {
    margin-top: 17px; font-size: 21px; font-weight: 700;
    color: var(--brand-green); line-height: 1;
  }
  .person-title {
    margin-top: 2px; font-size: 11.5px; font-weight: 500;
    color: var(--brand-green); letter-spacing: 0.6px;
  }
  .address {
    position: absolute; left: 0; top: 174px; width: 100%;
    text-align: center; color: var(--ink-light);
    font-size: 11.5px; line-height: 16px; letter-spacing: 0.3px;
  }
  .address__icon { display: block; margin: 0 auto 11px; }
</style>
</head>
<body>
  <section class="card card--front">
    <span class="brand-name">Belan Systems</span>
  </section>

  <section class="card card--back">
    <header class="back-header">
      <span class="brand-name">Belan Systems</span>
    </header>
    <div class="name-band">
      <svg class="name-band__notch" width="36" height="14" viewBox="0 0 36 14">
        <polygon points="0,0 36,0 18,14" fill="var(--brand-green)"/>
      </svg>
      <p class="person-name">Gerald Vanholt</p>
      <p class="person-title">CEO / Geschäftsführer &amp; Inhaber</p>
    </div>
    <div class="address">
      <svg class="address__icon" width="14" height="18" viewBox="0 0 14 18" fill="none" stroke="var(--ink-light)" stroke-width="1.2">
        <path d="M7 17 C7 17 1 10.5 1 6.5 A6 6 0 0 1 13 6.5 C13 10.5 7 17 7 17 Z"/>
        <circle cx="7" cy="6.5" r="2.2"/>
      </svg>
      <p>Brindlewood Ave 41</p>
      <p>58207 Harrowfield</p>
    </div>
  </section>
</body>
</html>
```